Independence Day Graphics for Sale

I want to create 10 social media graphics (new Pictora size 4:5 (1080 x 1350 pixels) focusing on our July 4th Sale Graphics, using any of the pics attached. Use the attached pics, NO RANDOM STOCK PHOTOGRAPHY. For the color scheme of the graphics, they should all be complementary to the product colors in the photos.
You can add any of the photos attached but none are required. You can do some of the graphics in all text. I mainly need BOLD text that says one of the headlines (10 total) SEE ATTACHED WORD DOCUMENT for the headlines to use.

Target Market(s)

women looking to lose weight

Requirements
Must have
• pics attached and text attached

```html
<!DOCTYPE html>
<html lang="en">
<head>
<meta charset="utf-8">
<title>Independence Day Sale Graphics</title>
<link rel="stylesheet" href="https://fonts.googleapis.com/css2?family=Bebas+Neue&family=Oswald:wght@300;400;500&display=swap">
<style>
  :root {
    --navy: #2e3192;
    --magenta: #c4288a;
    --page: #ffffff;
    --tile-light: #f1e6f1;
    --tile-deep: #c9a3d2;
    --photo-light: #f4eef4;
    --photo-mid: #d9c3dc;
    --ring: rgba(255, 255, 255, 0.55);
  }
  * { margin: 0; padding: 0; box-sizing: border-box; }
  html, body { width: 1200px; height: 600px; overflow: hidden; background: var(--page); }
  .sheet { position: relative; width: 1200px; height: 600px; }
  .tile {
    position: absolute; width: 218px; height: 273px; overflow: hidden;
    background: linear-gradient(160deg, var(--tile-light) 0%, #e2cde5 55%, var(--tile-deep) 100%);
  }
  .tile.soft { background: linear-gradient(180deg, var(--tile-light) 0%, #e6d5e9 60%, #f0e8f1 100%); }
  .col1 { left: 34px; } .col2 { left: 262px; } .col3 { left: 491px; } .col4 { left: 719px; } .col5 { left: 947px; }
  .row1 { top: 22px; } .row2 { top: 305px; }

  .line {
    position: absolute; left: 15px; white-space: nowrap; line-height: 1;
    font-family: "Bebas Neue", "Oswald", sans-serif; z-index: 2;
  }
  .line.center { left: 0; right: 0; text-align: center; }
  .navy { color: var(--navy); }
  .pink { color: var(--magenta); }
  .light { font-family: "Oswald", sans-serif; font-weight: 300; letter-spacing: -1px; transform: scaleX(0.86); transform-origin: left; }
  .light.center { transform-origin: center; }

  .photo {
    position: absolute; z-index: 1;
    background: linear-gradient(180deg, var(--photo-mid) 0%, var(--photo-light) 100%);
    border-radius: 2px; opacity: 0.85;
  }
  .photo.model { background: linear-gradient(180deg, rgba(217,195,220,0.2) 0%, rgba(244,238,244,0.9) 60%, var(--photo-light) 100%); }
  .ring { position: absolute; z-index: 0; }

  .offer-box {
    position: absolute; left: 14px; top: 135px; width: 190px; height: 73px;
    border: 1.5px solid var(--navy); z-index: 2;
    display: flex; align-items: center; justify-content: center;
    font-family: "Bebas Neue", sans-serif; font-size: 56px; color: var(--navy); line-height: 1; padding-top: 4px;
  }
</style>
</head>
<body>
<main class="sheet">

  <!-- July 4th mega sale -->
  <section class="tile col1 row1">
    <svg class="ring" width="218" height="273" viewBox="0 0 218 273"><circle cx="90" cy="110" r="95" fill="none" stroke="var(--ring)" stroke-width="1.2"/></svg>
    <div class="photo model" role="img" aria-label="Smiling woman in white cropped sweater holding a supplement bottle, bottles on table" style="left:115px;top:35px;width:103px;height:238px;"></div>
    <div class="line navy" style="top:14px;font-size:60px;">July 4th</div>
    <div class="line pink light" style="top:88px;font-size:46px;">MEGA</div>
    <div class="line pink light" style="top:131px;font-size:46px;">SALE!</div>
    <div class="line navy" style="top:198px;font-size:34px;">25% OFF</div>
    <div class="line navy" style="top:232px;font-size:24px;">EVERYTHING</div>
  </section>

  <!-- Biggest sale ever -->
  <section class="tile soft col2 row1">
    <div class="line navy" style="top:18px;font-size:29px;">BIGGEST 4TH OF JULY</div>
    <div class="line pink light" style="top:44px;font-size:50px;">SALE EVER!</div>
    <div class="line navy" style="top:100px;font-size:30px;">25% OFF SITEWIDE</div>
    <div class="photo" role="img" aria-label="Row of four white supplement bottles" style="left:15px;top:150px;width:190px;height:116px;"></div>
  </section>

  <!-- Historic sale -->
  <section class="tile soft col3 row1">
    <div class="line pink light center" style="top:34px;font-size:64px;">HISTORIC</div>
    <div class="line navy center" style="top:104px;font-size:31px;">4TH OF JULY SALE!</div>
    <div class="line navy center" style="top:145px;font-size:62px;">25% OFF</div>
    <div class="line pink center" style="top:218px;font-size:37px;">OF EVERYTHING</div>
  </section>

  <!-- Mega summer blowout -->
  <section class="tile col4 row1">
    <svg class="ring" width="218" height="273" viewBox="0 0 218 273"><circle cx="80" cy="160" r="85" fill="none" stroke="var(--ring)" stroke-width="1.2"/></svg>
    <div class="photo model" role="img" aria-label="Smiling woman behind a table lined with supplement bottles" style="left:100px;top:70px;width:118px;height:203px;"></div>
    <div class="line navy" style="top:16px;font-size:37px;">MEGA SUMMER</div>
    <div class="line navy" style="top:48px;font-size:37px;">BLOWOUT!</div>
    <div class="line pink light" style="top:100px;font-size:48px;">25%</div>
    <div class="line pink light" style="top:150px;font-size:48px;">OFF</div>
    <div class="line navy" style="top:200px;left:12px;font-size:19px;">EVERYTHING</div>
  </section>

  <!-- One-time only -->
  <section class="tile soft col5 row1">
    <div class="line pink light" style="top:12px;font-size:38px;">ONE-TIME ONLY:</div>
    <div class="line navy" style="top:55px;font-size:64px;">25% OFF</div>
    <div class="line navy" style="top:118px;font-size:37px;">OF EVERYTHING!</div>
    <div class="photo" role="img" aria-label="Row of four white supplement bottles" style="left:15px;top:160px;width:190px;height:110px;"></div>
  </section>

  <!-- Stock-up event -->
  <section class="tile soft col1 row2">
    <div class="line pink light center" style="top:20px;font-size:64px;">25% OFF</div>
    <div class="line pink light center" style="top:88px;font-size:37px;">STOCK-UP EVENT:</div>
    <div class="offer-box">25% OFF</div>
    <div class="line navy center" style="top:228px;font-size:33px;">ALL SUPPLEMENTS</div>
  </section>

  <!-- Lowest prices -->
  <section class="tile soft col2 row2">
    <div class="line pink light center" style="top:10px;font-size:45px;">THE LOWEST</div>
    <div class="line pink light center" style="top:57px;font-size:45px;">PRICES</div>
    <div class="line navy center" style="top:110px;font-size:29px;">WE'VE EVER OFFERED!</div>
    <div class="line navy center" style="top:140px;font-size:37px;">25% OFF</div>
    <div class="photo" role="img" aria-label="Row of four white supplement bottles" style="left:12px;top:180px;width:195px;height:93px;"></div>
  </section>

  <!-- Biggest discount -->
  <section class="tile soft col3 row2">
    <div class="line pink light center" style="top:10px;font-size:44px;">OUR BIGGEST</div>
    <div class="line navy center" style="top:57px;font-size:35px;">DISCOUNT EVER!</div>
    <div class="line navy center" style="top:95px;font-size:62px;">25% OFF</div>
    <div class="line navy center" style="top:152px;font-size:26px;">EVERYTHING</div>
    <div class="photo" role="img" aria-label="Row of four white supplement bottles" style="left:22px;top:178px;width:175px;height:95px;"></div>
  </section>

  <!-- Don't wait -->
  <section class="tile col4 row2">
    <svg class="ring" width="218" height="273" viewBox="0 0 218 273"><circle cx="90" cy="160" r="88" fill="none" stroke="var(--ring)" stroke-width="1.2"/></svg>
    <div class="photo model" role="img" aria-label="Smiling woman behind a table with three supplement bottles" style="left:90px;top:30px;width:128px;height:243px;"></div>
    <div class="line navy" style="top:12px;left:12px;font-size:50px;">DON'T WAIT!</div>
    <div class="line pink light" style="top:65px;left:12px;font-size:52px;">25%</div>
    <div class="line pink light" style="top:115px;left:12px;font-size:52px;">OFF</div>
    <div class="line navy" style="top:183px;left:12px;font-size:36px;">ENDS</div>
    <div class="line navy" style="top:217px;left:12px;font-size:36px;">SOON</div>
  </section>

  <!-- Last chance -->
  <section class="tile col5 row2">
    <svg class="ring" width="218" height="273" viewBox="0 0 218 273"><circle cx="100" cy="150" r="90" fill="none" stroke="var(--ring)" stroke-width="1.2"/></svg>
    <div class="photo model" role="img" aria-label="Smiling woman holding a supplement bottle, bottles on table" style="left:105px;top:35px;width:113px;height:238px;"></div>
    <div class="line navy" style="top:15px;left:14px;font-size:43px;">LAST CHANCE</div>
    <div class="line pink light" style="top:67px;left:14px;font-size:48px;">25%</div>
    <div class="line pink light" style="top:117px;left:14px;font-size:48px;">OFF</div>
    <div class="line navy" style="top:188px;left:14px;font-size:28px;">TIME IS</div>
    <div class="line navy" style="top:213px;left:14px;font-size:28px;">RUNNING</div>
    <div class="line navy" style="top:238px;left:14px;font-size:28px;">OUT!</div>
  </section>

</main>
</body>
</html>
```